Letterhead Design Project

Based on the attached logo we would like have a designed of stationary.
As we are a management consulting company focused on business development dealing with C-level and one level below we new business cards.
We have decided to use KRM (Northvale Advisory Partners) as the business name. The legal name will be Northvale Advisory Partners ApS but we will brand us under KRM. The tack line is “Shaping Lasting Gains” if we need one.
For legal reasons we need to have the legal name on the letters together with the company no. (cvr. nr. 58190476)
We want to signal the following:
- Serious
- Professional
- Creating Result
- Capable of thinking out of the box and creative
- Fast reactions we will be there when needed
What we do not want to be view as is:
- To smart
- We know better
- We can fix it yesterday
Our Value Proposition is two sited:
- Increasing revenue
- Reduced sales cost or increased efficiency
Therefore, companies can call us when they want to grow or they need to be more efficient.
Our business cards should have a two sided print with the logo incl. the tack line on one side and the detailed information on the other site.
We need to have the following information on the letter head:
- Legal company name
- Cvr nr.
- Address incl. country name (Denmark)
- Main number
- Wed address
Symbols are welcome to be used to guide for the above information.
The following information are expected to be in the personal signature of the letter.
- Name
- Title
- Mobile number
- E-mail address
Updates
Some of you has requested our specific details so here they come:
- Address incl. country name (Denmark): Lyngholmvej 42, 2950 Vedbæk, Denmark
- Main number: +45 7381 5502
- Wed address: www.krmgrowth.com
Mobile no. are +45 xxxx xxxx or +45 2857 3016
Our e-mail looks like this: firstname.seconname@KRMGROWTH.COM or for me: henrik.dalgaard@krmgrowth.com
We need the design (file) as finish as posible so we just need to add personal details before printing.
Please be aware that we will prefer designs where we can print the full letter incl. design. As we are communicating on e-mails with pdf versions of the letter we also need to have a design which will print on the clients printers.
Target Market(s)
C level and one level below.
Major local and international Companies.
Industry/Entity Type
Management Consulting
Font styles to use
Colors
Designer to choose colors to be used in the design.
Requirements
Must have
- Use of our logo without tack line

```html
<!DOCTYPE html>
<html lang="en">
<head>
<meta charset="utf-8">
<title>KRM Letterhead</title>
<link href="https://fonts.googleapis.com/css2?family=Quicksand:wght@500;700&display=swap" rel="stylesheet">
<style>
  :root {
    --backdrop: #3a3a3a;
    --paper: #ffffff;
    --ink-grey: #6d6d6d;
    --heading-grey: #6b6b6b;
    --brand-blue: #1a5fb4;
    --rule-blue: #8aa9d3;
    --signature-tone: #c9d3ea;
  }
  * { margin: 0; padding: 0; box-sizing: border-box; }
  html, body { width: 1200px; height: 1000px; overflow: hidden; }
  body {
    background: var(--backdrop);
    font-family: "Quicksand", sans-serif;
    position: relative;
  }
  .letter-page {
    position: absolute;
    left: 268px; top: 11px;
    width: 687px; height: 969px;
    background: var(--paper);
  }
  .brand-name {
    position: absolute;
    right: 42px; top: 46px;
    display: flex; align-items: center; gap: 10px;
    font-size: 58px; font-weight: 700;
    color: var(--brand-blue);
    letter-spacing: -1px;
    line-height: 1;
  }
  .brand-dot {
    width: 16px; height: 16px; border-radius: 50%;
    background: var(--brand-blue);
  }
  .letter-body {
    position: absolute;
    left: 48px; top: 260px;
    width: 605px;
    color: var(--ink-grey);
  }
  .letter-heading {
    font-size: 17px; font-weight: 700;
    color: var(--heading-grey);
    line-height: 22px;
    margin-bottom: 12px;
  }
  .letter-body p {
    font-size: 12px; font-weight: 500;
    line-height: 13.6px;
    letter-spacing: -0.4px;
    text-align: justify;
    hyphens: auto;
    margin-bottom: 13.6px;
  }
  .sender-block {
    position: absolute;
    left: 48px; top: 778px;
    color: var(--brand-blue);
  }
  .signature-mark {
    width: 94px; height: 28px;
    background: var(--signature-tone);
    border-radius: 3px;
    margin-bottom: 8px;
  }
  .sender-name { font-size: 12.5px; font-weight: 700; line-height: 16px; }
  .sender-title { font-size: 10.5px; font-weight: 500; line-height: 14px; margin-bottom: 6px; }
  .sender-contact { font-size: 10.5px; font-weight: 500; line-height: 13.5px; }
  .footer-rule {
    position: absolute;
    left: 22px; right: 23px; top: 920px;
    height: 1px; background: var(--rule-blue);
  }
  .footer-line {
    position: absolute;
    left: 22px; right: 23px; top: 926px;
    display: flex; justify-content: space-between; align-items: center;
    font-size: 9.2px; font-weight: 500;
    color: var(--brand-blue);
  }
  .footer-item { display: flex; align-items: center; gap: 6px; white-space: nowrap; }
  .footer-item svg { width: 15px; height: 15px; }
</style>
</head>
<body>
  <main class="letter-page">
    <div class="brand-name"><span class="brand-dot"></span>KRM</div>

    <section class="letter-body" lang="en">
      <h1 class="letter-heading">Sample Text</h1>
      <p>Lorem ipsum dolor sit amet, consectetur adipiscing elit. Pellentesque ornare enim a tristique aliquet. Aliquam congue, urna at ultrices venenatis, dolor diam ultricies felis, sed placerat ante lacus dignissim mi. Integer a suscipit erat, at vestibulum arcu. Nulla blandit lectus augue, sed dapibus lorem laoreet nec. Donec nulla nisl, rutrum eu tincidunt id, pharetra vitae metus. Cum sociis natoque penatibus et magnis dis parturient montes, nascetur ridiculus mus. Pellentesque feugiat pulvinar tortor, eu fermentum tellus elementum id.</p>
      <p>Duis sit amet velit mi. Sed accumsan lacus non lacus imperdiet congue. Morbi ac sapien sed urna ornare venenatis eget sed diam. Duis turpis risus, ullamcorper ut arcu non, suscipit adipiscing leo. Etiam auctor aliquam luctus. Aenean vestibulum sapien nec enim aliquam accumsan. Integer fringilla ac augue fringilla hendrerit. Sed porttitor sollicitudin sem, ut laoreet metus volutpat ut.</p>
      <p>Nulla venenatis nibh vel mattis accumsan. Proin consectetur adipiscing dui ac convallis. Praesent vitae est dignissim, pretium nulla non, eleifend velit. Maecenas pulvinar, nisl at venenatis placerat, felis leo scelerisque mauris, vel luctus magna massa nec lorem. Sed sed lorem lectus. Fusce suscipit turpis vitae neque eleifend mattis. Etiam hendrerit vitae ligula et elementum. Nunc quis lobortis lacus. Integer eleifend quam dolor, et pulvinar lectus sodales eget. Quisque ultricies arcu quis vulputate accumsan.</p>
      <p>Lorem ipsum dolor sit amet, consectetur adipiscing elit. Pellentesque ornare enim a tristique aliquet. Aliquam congue, urna at ultrices venenatis, dolor diam ultricies felis, sed placerat ante lacus dignissim mi. Integer a suscipit erat, at vestibulum arcu. Nulla blandit lectus augue, sed dapibus lorem laoreet nec. Donec nulla nisl, rutrum eu tincidunt id, pharetra vitae metus. Cum sociis natoque penatibus et magnis dis parturient montes, nascetur ridiculus mus. Pellentesque feugiat pulvinar tortor, eu fermentum tellus elementum id.</p>
      <p>Duis sit amet velit mi. Sed accumsan lacus non lacus imperdiet congue. Morbi ac sapien sed urna ornare venenatis eget sed diam. Duis turpis risus, ullamcorper ut arcu non, suscipit adipiscing leo. Etiam auctor aliquam luctus. Aenean vestibulum sapien nec enim aliquam accumsan. Integer fringilla ac augue fringilla hendrerit. Sed porttitor sollicitudin sem, ut laoreet metus volutpat ut.</p>
    </section>

    <section class="sender-block">
      <div class="signature-mark" role="img" aria-label="Handwritten signature of the sender"></div>
      <div class="sender-name">Mikkel Sørvang</div>
      <div class="sender-title">Title</div>
      <div class="sender-contact">Mobil/direct: +45 xxxx xxxx</div>
      <div class="sender-contact">E-mail: xxxxxx.xxxxxx@krmgrowth.com</div>
    </section>

    <div class="footer-rule"></div>
    <footer class="footer-line">
      <span class="footer-item">Northvale Advisory Partners ApS, CVR: 58 19 04 76</span>
      <span class="footer-item">
        <svg viewBox="0 0 16 16" fill="none" stroke="currentColor" stroke-width="1.1"><circle cx="8" cy="8" r="7.2"/><path d="M8 12.5 C6 10 5.2 8.6 5.2 7 A2.8 2.8 0 0 1 10.8 7 C10.8 8.6 10 10 8 12.5Z"/><circle cx="8" cy="7" r="1"/></svg>
        Lyngholmvej 42, 2950 Vedbæk, Denmark
      </span>
      <span class="footer-item">
        <svg viewBox="0 0 16 16" fill="none" stroke="currentColor" stroke-width="1.1"><circle cx="8" cy="8" r="7.2"/><path d="M5.3 4.5 L6.6 4.3 L7.3 6.2 L6.5 7 C7 8.1 7.9 9 9 9.5 L9.8 8.7 L11.7 9.4 L11.5 10.7 C8 11 5 8 5.3 4.5Z"/></svg>
        +45 7381 5502
      </span>
      <span class="footer-item">
        <svg viewBox="0 0 16 16" fill="none" stroke="currentColor" stroke-width="1.1"><circle cx="8" cy="8" r="7"/><ellipse cx="8" cy="8" rx="3" ry="7"/><path d="M1 8 H15 M2 4.5 H14 M2 11.5 H14"/></svg>
        www.krmgrowth.com
      </span>
    </footer>
  </main>
</body>
</html>
```